Gutschein-Design Falter Webshop
Zielgruppe
Webshop von Pyrotechnischen Artikeln. Rauchkörper, Bengalische Lichter, Kinderfeuerwerk, klassisches Silvesterfeuerwerk. Der Shop ist zu finden unter https://www.funkenkiste-beispiel.de
Das Format sollte sich an DIN Lang orientieren.
Wenn Artikelbilder oder sonstige Fotos aus dem Shop benötigt werden, können diese gerne angefragt werden.
Aufgabenstellung
Der Shop sollte im Flyer wieder erkennbar sein und nach Möglichkeit alle 5 Hauptkategorien abbilden.
Wobei Silvesterfeuerwerk, Zubehör und Partyartikel die kleinere Rolle spielen.
Rauch und Bengal stehen dabei im Vordergrund
Ein Textfeld sollte enthalten sein, worein wir dann den Gutscheincode / Wert drucken.
Edit: Sorry, ich hatte anfangs die falschen Grafiken hochgeladen. Jetzt ist das Shoplogo in den Files zu finden. Ebenso ein Beispielfoto mit Rauch

```html
<!DOCTYPE html>
<html lang="de">
<head>
<meta charset="utf-8">
<title>Gutschein – Falter Webshop</title>
<link href="https://fonts.googleapis.com/css2?family=Archivo+Black&family=Open+Sans:wght@400;600&display=swap" rel="stylesheet">
<style>
  :root {
    --orange: #f5a623;
    --brand: #c9943a;
    --nav-text: #4a5560;
    --grey-text: #555;
    --url-text: #666;
    --rule: #e6e6e6;
    --white: #ffffff;
  }
  * { margin: 0; padding: 0; box-sizing: border-box; }
  html, body { width: 1016px; height: 1200px; overflow: hidden; background: var(--white); }
  body { position: relative; font-family: "Open Sans", sans-serif; color: var(--grey-text); }

  .front, .back { position: absolute; left: 0; width: 1016px; }
  .front { top: 0; height: 506px; }
  .back { top: 707px; height: 493px; border-top: 3px solid var(--rule); }

  .smoke-header {
    position: absolute; left: 0; top: 0; width: 100%; height: 196px;
    background:
      radial-gradient(ellipse 300px 90px at 120px 170px, rgba(233,170,30,.85), transparent 70%),
      radial-gradient(ellipse 260px 70px at 430px 150px, rgba(240,130,70,.7), transparent 70%),
      radial-gradient(ellipse 320px 80px at 820px 165px, rgba(232,70,100,.75), transparent 70%),
      linear-gradient(to bottom, #fff 40%, rgba(255,255,255,0) 100%);
  }
  .brand {
    position: absolute; display: flex; align-items: center; gap: 8px;
    font-weight: 600; color: var(--brand); font-size: 30px; line-height: 1;
  }
  .brand .mark { width: 14px; height: 14px; background: var(--brand); }
  .front .brand { left: 48px; top: 54px; }
  .back .brand { right: 44px; top: 62px; }

  .nav { position: absolute; left: 0; width: 100%; }
  .front .nav { top: 196px; height: 51px; background: var(--white); }
  .back .nav { top: 125px; height: 41px; border-bottom: 2px solid var(--orange); }
  .nav-list { position: relative; list-style: none; height: 100%; }
  .nav-item {
    position: absolute; bottom: 0; height: 39px; line-height: 39px;
    font-size: 16px; font-weight: 600; color: var(--nav-text); white-space: nowrap;
  }
  .nav-item.home { display: flex; align-items: center; }
  .nav-item.active {
    background: var(--orange); color: var(--white); border-radius: 3px 3px 0 0;
    width: 81px; text-align: center;
  }
  .front .home { left: 148px; } .front .active { left: 191px; }
  .front .i-rauch { left: 291px; } .front .i-party { left: 422px; }
  .front .i-feuer { left: 542px; } .front .i-zubehoer { left: 654px; }
  .back .home { left: 133px; } .back .active { left: 176px; }
  .back .i-rauch { left: 276px; } .back .i-party { left: 407px; }
  .back .i-feuer { left: 527px; } .back .i-zubehoer { left: 640px; }

  .web {
    position: absolute; right: 51px; top: 9px; line-height: 30px;
    font-size: 18px; color: var(--url-text); white-space: nowrap;
  }

  .smoke-band {
    position: absolute; left: 0; top: 248px; width: 100%; height: 254px;
    background:
      radial-gradient(ellipse 260px 170px at 110px 120px, rgba(232,60,80,.85), transparent 72%),
      radial-gradient(ellipse 260px 140px at 400px 40px, rgba(200,80,140,.55), transparent 72%),
      radial-gradient(ellipse 240px 130px at 620px 60px, rgba(120,70,110,.6), transparent 72%),
      radial-gradient(ellipse 260px 200px at 880px 130px, rgba(40,170,210,.85), transparent 72%),
      linear-gradient(#fff, #fff);
  }
  .title {
    position: absolute; left: 44px; display: inline-block;
    font-family: "Archivo Black", sans-serif; font-size: 124px; line-height: 1;
    text-transform: uppercase; letter-spacing: -4px; white-space: nowrap;
    transform: scaleX(0.82); transform-origin: left top;
  }
  .front-title { top: 234px; color: var(--white); }
  .back-title {
    top: 170px;
    background: linear-gradient(90deg, #e4a51c 0%, #e9891f 30%, #f2a07a 48%, #ee5c55 68%, #ea3f5c 100%);
    -webkit-background-clip: text; background-clip: text; color: transparent;
  }
  .front-rule { position: absolute; left: 0; top: 502px; width: 100%; height: 4px; background: var(--rule); }

  .contact {
    position: absolute; right: 51px; top: 192px; text-align: right;
    font-size: 13px; line-height: 16.5px; color: var(--grey-text); font-style: normal;
  }
  .contact p + p { margin-top: 16px; }

  .value-field {
    position: absolute; left: 174px; top: 356px; width: 82px; height: 137px;
    background: var(--orange); border-radius: 6px 6px 0 0;
    color: var(--white); font-weight: 600; font-size: 15px; line-height: 19px;
    text-align: right; padding: 6px 14px 0 8px;
  }
</style>
</head>
<body>

<section class="front">
  <div class="smoke-header" role="img" aria-label="Farbiger Rauch in Gelb, Orange und Rot"></div>
  <div class="brand"><span class="mark"></span>funkenkiste</div>
  <nav class="nav">
    <ul class="nav-list">
      <li class="nav-item home">
        <svg width="22" height="20" viewBox="0 0 22 20" aria-hidden="true"><path d="M11 1 L1 10 L4 10 L4 19 L9 19 L9 13 L13 13 L13 19 L18 19 L18 10 L21 10 Z" fill="#2f3a44"/></svg>
      </li>
      <li class="nav-item active">Bengal</li>
      <li class="nav-item i-rauch">Rauchkörper</li>
      <li class="nav-item i-party">Partyartikel</li>
      <li class="nav-item i-feuer">Feuerwerk</li>
      <li class="nav-item i-zubehoer">Zubehör</li>
    </ul>
  </nav>
  <div class="smoke-band" role="img" aria-label="Farbiger Rauch von Rot über Violett bis Blau"></div>
  <h1 class="title front-title">Gutschein</h1>
  <div class="front-rule"></div>
</section>

<section class="back">
  <div class="brand"><span class="mark"></span>funkenkiste</div>
  <nav class="nav">
    <ul class="nav-list">
      <li class="nav-item home">
        <svg width="22" height="20" viewBox="0 0 22 20" aria-hidden="true"><path d="M11 1 L1 10 L4 10 L4 19 L9 19 L9 13 L13 13 L13 19 L18 19 L18 10 L21 10 Z" fill="#2f3a44"/></svg>
      </li>
      <li class="nav-item active">Bengal</li>
      <li class="nav-item i-rauch">Rauchkörper</li>
      <li class="nav-item i-party">Partyartikel</li>
      <li class="nav-item i-feuer">Feuerwerk</li>
      <li class="nav-item i-zubehoer">Zubehör</li>
    </ul>
    <div class="web">www.funkenkiste-beispiel.de</div>
  </nav>
  <h2 class="title back-title">Gutschein</h2>
  <address class="contact">
    <p>Hellmann &amp; Roth GbR<br>Lindenweg 12<br>15500 Musterfeld</p>
    <p>Telefon: 03300.123450<br>Telefax: 03300.123451<br>E-Mail: info@funkenkiste-beispiel.de</p>
  </address>
  <div class="value-field">im Wert von:</div>
</section>

</body>
</html>
```